■依頼の目的/概要
当方販促で使用するメモ帳を販売しております。
年間と通じて企業様が挨拶に出向く時に使用するノベルティメモ帳の表紙のデザインをお願いします。

■依頼詳細
貰って嬉しいメモ帳の表紙を提案下さい。今扱っている実績デザインを添付いたします。

■重視するポイント
色使いなど制限はありませんが、貰ってうれしい配って嬉しいデザインを要望します。今扱っているメモ帳デザインの一部を添付いたしますが、全く新しいデザインを希望します。テンプレートを添付しておりますのでご利用下さい。また、いい提案がありましたら複数個採用いたします。

その他何かご不明な点がございましたら、お気軽にご質問下さい。
よろしくお願いいたします。
ランサーの皆様、今回たくさんのご提案ありがとうございました。来週中には複数個の採用予定しております。選定までもうしばらくお待ち下さいませ。

社内アンケートを行って決定しました。一息つけるデザインと若者受けする和風なデザインが選ばれたように思います。

今回の依頼でたくさんのランサーの皆様のご提案ありがとうございます。せっかく時間を割いて提案して下さったにも関わらず選択されなかったランサー様には申し訳けなく思っております。近々またメモ帳の表紙デザインを現在依頼する予定もあります。よろしければご提案下さいませ。

```html
<!DOCTYPE html>
<html lang="ja">
<head>
<meta charset="utf-8">
<title>メモ帳 表紙デザイン</title>
<link href="https://fonts.googleapis.com/css2?family=M+PLUS+Rounded+1c:wght@800&display=swap" rel="stylesheet">
<style>
  :root {
    --paper: #ffffff;
    --ink: #111111;
    --trim: #999999;
    --bulb-yellow: #f2c75c;
    --ray-yellow: #f6d98c;
    --bulb-grey: #8a8a8a;
  }
  html, body {
    margin: 0;
    padding: 0;
    width: 1200px;
    height: 3036px;
    overflow: hidden;
    background: var(--paper);
  }
  .sheet {
    position: relative;
    width: 1200px;
    height: 3036px;
    background: var(--paper);
    font-family: "M PLUS Rounded 1c", sans-serif;
    color: var(--ink);
  }
  .crop-marks {
    position: absolute;
    inset: 0;
  }
  .cover {
    position: absolute;
    left: 124px;
    width: 952px;
    height: 1364px;
    border: 3px solid var(--ink);
    box-sizing: border-box;
    background: var(--paper);
  }
  .cover--back { top: 124px; }
  .cover--front { top: 1538px; }

  .memo-word {
    position: absolute;
    font-weight: 800;
    line-height: 1;
    transform: translate(-50%, -50%) rotate(180deg);
    white-space: nowrap;
    letter-spacing: -0.01em;
  }
  .memo-word--s { font-size: 36px; }
  .memo-word--m { font-size: 60px; }
  .memo-word--l { font-size: 88px; }

  .idea-art {
    position: absolute;
    left: 152px;
    top: 292px;
    width: 660px;
    height: 700px;
    border-radius: 48px;
    background:
      radial-gradient(ellipse 34% 30% at 50% 58%, var(--bulb-yellow) 0%, var(--bulb-yellow) 70%, rgba(242,199,92,0) 100%),
      linear-gradient(180deg, var(--ray-yellow) 0%, #fbeec8 55%, #e9e3d6 82%, var(--bulb-grey) 100%);
  }
  .tagline {
    position: absolute;
    left: 0;
    right: 0;
    top: 1024px;
    margin: 0;
    text-align: center;
    font-size: 84px;
    line-height: 1;
    font-weight: 800;
    letter-spacing: 0.02em;
  }
</style>
</head>
<body>
<div class="sheet">
  <svg class="crop-marks" width="1200" height="3036" viewBox="0 0 1200 3036" aria-hidden="true">
    <g stroke="var(--trim)" stroke-width="2" fill="none">
      <path d="M0 80H124 M0 124H80 M80 0V124 M124 0V80"/>
      <path d="M1200 80H1076 M1200 124H1120 M1120 0V124 M1076 0V80"/>
      <path d="M0 2956H124 M0 2912H80 M80 3036V2912 M124 3036V2956"/>
      <path d="M1200 2956H1076 M1200 2912H1120 M1120 3036V2912 M1076 3036V2956"/>
      <path d="M600 0V100 M480 60H720 M480 20V100 M720 20V100"/>
      <path d="M600 3036V2936 M480 2976H720 M480 2936V3016 M720 2936V3016"/>
      <path d="M40 1390V1650 M0 1512H100 M0 1488H80 M0 1536H80"/>
      <path d="M1160 1390V1650 M1200 1512H1100 M1200 1488H1120 M1200 1536H1120"/>
    </g>
  </svg>

  <section class="cover cover--back" aria-label="裏表紙">
    <span class="memo-word memo-word--m" style="left:436px;top:530px;">memo</span>
    <span class="memo-word memo-word--s" style="left:396px;top:590px;">memo</span>
    <span class="memo-word memo-word--m" style="left:586px;top:588px;">memo</span>
    <span class="memo-word memo-word--l" style="left:300px;top:650px;">memo</span>
    <span class="memo-word memo-word--s" style="left:500px;top:656px;">memo</span>
    <span class="memo-word memo-word--s" style="left:256px;top:716px;">memo</span>
    <span class="memo-word memo-word--m" style="left:436px;top:716px;">memo</span>
    <span class="memo-word memo-word--s" style="left:636px;top:718px;">memo</span>
    <span class="memo-word memo-word--s" style="left:416px;top:780px;">memo</span>
    <span class="memo-word memo-word--l" style="left:626px;top:792px;">memo</span>
  </section>

  <section class="cover cover--front" aria-label="表表紙">
    <div class="idea-art" role="img" aria-label="黄色い光線に囲まれた、灰色の口金付きの黄色い電球のイラスト"></div>
    <p class="tagline">Inspiration</p>
  </section>
</div>
</body>
</html>
```